Business Card design for Brightvale Global

we need a business card design for our company. we are a trading company based in LA.

Company Name: Brightvale Global Corp.
Contact: Marcus Ortega
Title: CEO
Tel: 310-647-2093
Email: bvgcorp7@mailnest.example

Target Market(s)

International, especially China

Industry/Entity Type

Trade

Colors
3276b5
34a7d8
0555a3
0493ce
85cae6
85acd3
d0dfed
cee9f5

Requirements
Must have
• Logo and contact, to have international/global feeling

```html
<!DOCTYPE html>
<html lang="en">
<head>
<meta charset="utf-8">
<title>Brightvale Global – Business Card</title>
<link rel="stylesheet" href="https://fonts.googleapis.com/css2?family=Lato:wght@400;700&display=swap">
<style>
  :root {
    --backdrop: #1d1d1f;
    --navy: #1a3764;
    --navy-soft: #23477b;
    --brand-blue: #3276b5;
    --sky: #2aa8df;
    --slate: #555b63;
    --paper: #ffffff;
    --ice: #cee9f5;
  }
  * { margin: 0; padding: 0; box-sizing: border-box; }
  html, body {
    width: 1200px; height: 897px; overflow: hidden;
    background: var(--backdrop);
    font-family: "Lato", Arial, sans-serif;
  }
  .card {
    position: absolute; left: 304px; width: 594px; height: 338px;
    border-radius: 22px; overflow: hidden;
  }
  .card--front { top: 92px; background: var(--paper); }
  .card--back { top: 470px; background: var(--navy); }

  .wave { position: absolute; inset: 0; width: 594px; height: 338px; }

  .brand { position: absolute; display: flex; align-items: center; gap: 12px; }
  .brand__dot { width: 44px; height: 44px; border-radius: 50%; flex: none; }
  .brand__name { font-weight: 700; line-height: 1; }
  .brand__name span { display: block; }
  .brand__word { font-size: 40px; }
  .brand__sub { font-size: 14px; letter-spacing: 10px; margin-top: 6px; }

  .card--front .brand { left: 30px; top: 92px; }
  .card--front .brand__dot { background: var(--brand-blue); }
  .card--front .brand__name { color: var(--brand-blue); }

  .holder { position: absolute; right: 38px; top: 86px; text-align: right; }
  .holder__name { font-size: 21px; font-weight: 700; color: var(--brand-blue); letter-spacing: 1px; }
  .holder__title { font-size: 15px; color: var(--slate); margin-top: 2px; }

  .contacts { position: absolute; right: 38px; top: 250px; list-style: none; }
  .contacts li {
    display: flex; align-items: center; justify-content: flex-end; gap: 10px;
    color: var(--paper); font-size: 14px; height: 19.5px;
  }
  .contacts svg { width: 11px; height: 11px; flex: none; }

  .world-map {
    position: absolute; left: 48px; top: 6px; width: 500px; height: 304px;
    background: radial-gradient(ellipse at center, var(--navy-soft) 0%, rgba(35,71,123,0.35) 60%, rgba(26,55,100,0) 80%);
  }
  .card--back .brand { left: 50%; top: 128px; transform: translateX(-50%); }
  .card--back .brand__dot { background: var(--paper); width: 52px; height: 52px; }
  .card--back .brand__name { color: var(--paper); }
  .card--back .brand__word { font-size: 48px; }
  .card--back .brand__sub { font-size: 16px; letter-spacing: 12px; }

  .web {
    position: absolute; left: 0; right: 0; top: 292px; text-align: center;
    color: var(--paper); font-size: 15px; letter-spacing: 1.5px;
  }
</style>
</head>
<body>

<section class="card card--front">
  <svg class="wave" viewBox="0 0 594 338" aria-hidden="true">
    <path fill="#1a3764" d="M0,282 C50,318 110,336 180,334 C260,332 320,232 594,222 L594,338 L0,338 Z"/>
    <path fill="#2aa8df" d="M176,330 C256,322 316,206 594,194 L594,212 C318,222 262,324 176,330 Z"/>
  </svg>

  <div class="brand">
    <span class="brand__dot"></span>
    <div class="brand__name">
      <span class="brand__word">Brightvale</span>
      <span class="brand__sub">GLOBAL</span>
    </div>
  </div>

  <div class="holder">
    <div class="holder__name">MARCUS ORTEGA</div>
    <div class="holder__title">CEO</div>
  </div>

  <ul class="contacts">
    <li>310-647-2093
      <svg viewBox="0 0 24 24"><path fill="#2aa8df" d="M6.6 10.8a15 15 0 0 0 6.6 6.6l2.2-2.2a1 1 0 0 1 1-.25 11.4 11.4 0 0 0 3.6.6 1 1 0 0 1 1 1V20a1 1 0 0 1-1 1A17 17 0 0 1 3 4a1 1 0 0 1 1-1h3.5a1 1 0 0 1 1 1c0 1.25.2 2.450.6 3.6a1 1 0 0 1-.25 1Z"/></svg>
    </li>
    <li>bvgcorp7@mailnest.example
      <svg viewBox="0 0 24 24"><path fill="#2aa8df" d="M2 5h20v14H2Z M2 5l10 8 10-8" stroke="#1a3764" stroke-width="1.5"/></svg>
    </li>
    <li>brightvaleglobal.example
      <svg viewBox="0 0 24 24"><g fill="none" stroke="#2aa8df" stroke-width="2"><circle cx="12" cy="12" r="10"/><path d="M2 12h20M12 2c3 3 3 17 0 20M12 2c-3 3-3 17 0 20"/></g></svg>
    </li>
  </ul>
</section>

<section class="card card--back">
  <div class="world-map" role="img" aria-label="Dotted world map in a slightly lighter navy behind the company name"></div>

  <div class="brand">
    <span class="brand__dot"></span>
    <div class="brand__name">
      <span class="brand__word">Brightvale</span>
      <span class="brand__sub">GLOBAL</span>
    </div>
  </div>

  <div class="web">www.brightvaleglobal.example</div>
</section>

</body>
</html>
```